BRIVETTA Need a luxury modern business card designed.

Need a luxury modern business card designed. refer to the uploaded files for the company name and logo in the zip file under source files. i will making my descion on monday. so please send in before then so if we need to edit we will have the time. we have a trade show coming up and im on a deadline for printer.

Target Market(s)

high end clients

Contact Information for Business Card

Company nAme and logo. Calvin Moross Co-Founder / Project Manager Office # 416-555-7391 Cell # 416-555-0186 BRIVETTA.CA Calvin@brivetta.ca

Font styles to use
Other font styles liked:
• Modern

Requirements
Must have
• Company name and logo, contact info, using the black, gold and white color scheme.

```html
<!DOCTYPE html>
<html lang="en">
<head>
<meta charset="utf-8">
<title>BRIVETTA Business Card</title>
<link href="https://fonts.googleapis.com/css2?family=Roboto:wght@300;400;500&display=swap" rel="stylesheet">
<style>
  :root {
    --backdrop: #e9e9e7;
    --card: #333132;
    --card-edge: #b3a56c;
    --gold: #b29d62;
    --white: #f4f4f2;
    --muted: #8d8c8a;
  }
  * { margin: 0; padding: 0; box-sizing: border-box; }
  html, body {
    width: 1200px; height: 801px; overflow: hidden;
    background: var(--backdrop);
    font-family: "Roboto", Arial, sans-serif;
  }
  .sheet {
    width: 1200px; height: 801px;
    display: flex; align-items: center; justify-content: center; gap: 60px;
  }
  .card {
    width: 500px; height: 286px;
    background: var(--card);
    border: 3px solid var(--card-edge);
    border-radius: 3px;
    position: relative;
    box-shadow: 0 14px 30px rgba(0,0,0,0.18);
    color: var(--white);
  }
  /* Front */
  .card-front { display: flex; align-items: center; }
  .brand-block {
    width: 230px; height: 100%;
    display: flex; align-items: center; justify-content: center; gap: 10px;
  }
  .brand-square { width: 14px; height: 14px; background: var(--white); }
  .brand-name {
    font-weight: 300; font-size: 26px; letter-spacing: 4px; color: var(--white);
  }
  .divider { width: 1px; height: 120px; background: var(--muted); }
  .contact-block { padding-left: 30px; }
  .person-name { color: var(--gold); font-weight: 500; font-size: 19px; }
  .person-title { font-weight: 300; font-size: 13px; margin-top: 3px; }
  .contact-list { list-style: none; margin-top: 16px; }
  .contact-list li {
    display: flex; align-items: center; gap: 10px;
    font-weight: 300; font-size: 13px; line-height: 21px;
  }
  .contact-list svg { width: 12px; height: 12px; flex: none; }
  .accent { color: var(--gold); }
  /* Back */
  .card-back { display: flex; align-items: center; justify-content: flex-end; padding-right: 40px; }
  .card-back .brand-name { font-size: 38px; letter-spacing: 6px; }
  .card-back .brand-square { width: 18px; height: 18px; margin-right: 14px; }
</style>
</head>
<body>
<main class="sheet">
  <section class="card card-front">
    <div class="brand-block">
      <span class="brand-square"></span>
      <span class="brand-name">BRIVETTA</span>
    </div>
    <div class="divider"></div>
    <div class="contact-block">
      <p class="person-name">Calvin Moross</p>
      <p class="person-title">Co-Founder / Project Manager</p>
      <ul class="contact-list">
        <li>
          <svg viewBox="0 0 12 12"><path d="M2.5 1 L4.5 1 L5 3.5 L3.8 4.5 Q5 7 7.5 8.2 L8.5 7 L11 7.5 L11 9.5 Q10 11 8 10.8 Q2 9 1.2 3 Q1.2 1.5 2.5 1 Z" fill="var(--gold)"/></svg>
          416-555-7391
        </li>
        <li>
          <svg viewBox="0 0 12 12"><rect x="3" y="0.8" width="6" height="10.4" rx="1" fill="none" stroke="var(--gold)" stroke-width="1.2"/><circle cx="6" cy="9.4" r="0.7" fill="var(--gold)"/></svg>
          416-555-0186
        </li>
        <li>
          <svg viewBox="0 0 12 12"><rect x="0.8" y="2.5" width="10.4" height="7" fill="none" stroke="var(--gold)" stroke-width="1.2"/><path d="M0.8 2.5 L6 6.5 L11.2 2.5" fill="none" stroke="var(--gold)" stroke-width="1.2"/></svg>
          Calvin@brivetta.ca
        </li>
        <li>
          <svg viewBox="0 0 12 12"><circle cx="6" cy="6" r="5.2" fill="none" stroke="var(--gold)" stroke-width="1.1"/><ellipse cx="6" cy="6" rx="2.2" ry="5.2" fill="none" stroke="var(--gold)" stroke-width="1"/><path d="M0.8 6 H11.2 M1.8 3.4 H10.2 M1.8 8.6 H10.2" stroke="var(--gold)" stroke-width="0.9"/></svg>
          www.<span class="accent">BRIVETTA.CA</span>
        </li>
      </ul>
    </div>
  </section>

  <section class="card card-back">
    <span class="brand-square"></span>
    <span class="brand-name">BRIVETTA</span>
  </section>
</main>
</body>
</html>
```